Finance Product Agency Business Card Design

We're an agency that provides products (service contracts, gap insurance, tire and wheel, etc) and support to dealership finance departments. We specialize in training finance producers to maximize their potential and also keep them up to date on the ever changing compliance and legal landscape. I'll attach an image of our logo, excited to see what you all come up with. Would also be interested in discussing our new website design with the winner.

Target Market(s)

auto dealerships

Industry/Entity Type

Business

Contact Information for Business Card

Mark Dolvery
Phone 317.624.5583
Fax 855.472.3308
email Mark.Dolvery@brightlanecoverage.example

Requirements
Must have
• basic contact information
Nice to have
• looking for something professional but modern

```html
<!DOCTYPE html>
<html lang="en">
<head>
<meta charset="utf-8">
<title>Brightlane Coverage – Business Card</title>
<link href="https://fonts.googleapis.com/css2?family=Oswald:wght@500;600&family=Tinos&display=swap" rel="stylesheet">
<style>
  :root {
    --page: #d6d6d6;
    --card-white: #ffffff;
    --slate: #3f5f6b;
    --slate-dark: #2f4a55;
    --ink: #1c1c1c;
    --ink-soft: #3a3a3a;
  }
  * { margin: 0; padding: 0; box-sizing: border-box; }
  html, body { width: 1200px; height: 2332px; overflow: hidden; }
  body { background: var(--page); position: relative; }

  .card {
    position: absolute;
    left: 100px;
    width: 1000px;
    height: 567px;
    overflow: hidden;
    box-shadow: 0 6px 18px rgba(0,0,0,0.18);
  }
  .card-front { top: 520px; background: var(--card-white); }
  .card-back  { top: 1240px; background: var(--slate); }

  .brand {
    position: absolute;
    display: flex;
    align-items: center;
    gap: 22px;
  }
  .brand-dot {
    width: 110px; height: 110px;
    border-radius: 50%;
    flex: none;
  }
  .brand-name {
    font-family: "Oswald", sans-serif;
    font-weight: 600;
    font-size: 62px;
    line-height: 1;
    letter-spacing: 1px;
    text-transform: uppercase;
  }
  .card-front .brand { left: 390px; top: 40px; }
  .card-front .brand-dot { background: var(--slate); }
  .card-front .brand-name { color: var(--slate); }

  .card-back .brand { left: 530px; top: 360px; }
  .card-back .brand-dot { background: #ffffff; }
  .card-back .brand-name { color: #ffffff; }
  .card-back .brand-name span { display: block; }

  .holder-name {
    position: absolute;
    left: 62px; top: 296px;
    font-family: "Oswald", sans-serif;
    font-weight: 600;
    font-size: 34px;
    letter-spacing: 1px;
    color: var(--ink);
    text-transform: uppercase;
  }
  .name-rule {
    position: absolute;
    left: 62px; top: 345px;
    width: 884px; height: 4px;
    background: var(--ink);
  }
  .contact-list {
    position: absolute;
    left: 62px; top: 364px;
    list-style: none;
    font-family: "Tinos", serif;
    font-size: 30px;
    color: var(--ink-soft);
  }
  .contact-list li {
    display: flex; align-items: center; gap: 14px;
    height: 46px;
  }
  .contact-list svg { width: 26px; height: 26px; fill: var(--ink-soft); flex: none; }

  .front-band { position: absolute; left: 0; bottom: 0; width: 1000px; height: 60px; }
</style>
</head>
<body>

<section class="card card-front">
  <div class="brand">
    <div class="brand-dot"></div>
    <div class="brand-name">Brightlane<br>Coverage</div>
  </div>

  <div class="holder-name">Mark Dolvery</div>
  <div class="name-rule"></div>

  <ul class="contact-list">
    <li>
      <svg viewBox="0 0 24 24"><path d="M6.6 10.8a15.1 15.1 0 0 0 6.6 6.6l2.2-2.2c.3-.3.7-.4 1-.2 1.1.4 2.3.6 3.6.6.6 0 1 .4 1 1V20c0 .6-.4 1-1 1A17 17 0 0 1 3 4c0-.6.4-1 1-1h3.5c.6 0 1 .4 1 1 0 1.3.2 2.5.6 3.6.1.3 0 .7-.2 1z"/></svg>
      317.624.5583
    </li>
    <li>
      <svg viewBox="0 0 24 24"><path d="M6 2h9l3 3v4H6zM4 10h16a2 2 0 0 1 2 2v7H2v-7a2 2 0 0 1 2-2zm2 11h12v1H6z"/><rect x="6" y="13" width="4" height="2" fill="#fff"/></svg>
      855.472.3308
    </li>
    <li>
      <svg viewBox="0 0 24 24"><path d="M2 5h20v14H2zm2 2v.4l8 5.2 8-5.2V7zm0 2.8V17h16V9.8l-8 5.2z"/></svg>
      Mark.Dolvery@brightlanecoverage.example
    </li>
  </ul>

  <svg class="front-band" viewBox="0 0 1000 60" preserveAspectRatio="none">
    <polygon points="0,14 770,14 830,60 0,60" fill="var(--slate)"/>
    <polygon points="800,34 1000,34 1000,60 834,60" fill="var(--ink)"/>
  </svg>
</section>

<section class="card card-back">
  <div class="brand">
    <div class="brand-dot"></div>
    <div class="brand-name"><span>Brightlane</span><span>Coverage</span></div>
  </div>
</section>

</body>
</html>
```